Booklet for meditation CD to match existing CD cover

We need a design for a booklet that matches the meditation CD cover previously designed. It should look like it belongs to the CD as it will be inserted into the cover slot. I hope you can re-use some of the existing artwork. It should incorporate the logo and the text and probably the list of tracks as well. I have attached the original CD cover file, the logo file, photo file and the specs from the CD production company for the 8 page booklet. The spec also includes a cover spec. You can ignore that part. Please put all the text from the CD cover, as well as the track names and the credits from the CD cover into the booklet and the text describing the meditation in full which I have enclosed as a word file.

Target Market(s)

People interested in meditation and personal growth

Font styles to use
Serif

Colors
0555a3
876aae
a54499
e667a6
ee363c

Requirements
Must have
• must match the existing CD cover, must include logo and photo and text from CD cover
• Design, Fonts and colours should match CD cover.

```html
<!DOCTYPE html>
<html lang="en">
<head>
<meta charset="utf-8">
<title>The River of Presence Meditation – Booklet</title>
<link rel="stylesheet" href="https://fonts.googleapis.com/css2?family=Cinzel:wght@600&family=Roboto+Condensed:ital,wght@0,300;0,700;1,300;1,700&display=swap">
<style>
  :root {
    --page-bg: #ffffff;
    --ink: #120a16;
    --title-ink: #fdf4f1;
    --logo-purple: #876aae;
    --frame: #2a1c2e;
  }
  * { box-sizing: border-box; margin: 0; padding: 0; }
  html, body { width: 1200px; height: 1200px; overflow: hidden; background: var(--page-bg); }
  body { position: relative; font-family: "Roboto Condensed", "Arial Narrow", sans-serif; color: var(--ink); }

  .panel { position: absolute; overflow: hidden; }
  .panel--cover { left: 30px; top: 34px; width: 576px; height: 572px;
    background: linear-gradient(180deg, #3b1d46 0%, #8a2f63 30%, #c9577e 52%, #e59aa6 62%, #8e6a8f 72%, #6b5b78 100%); }
  .panel--intro { left: 608px; top: 34px; width: 575px; height: 572px;
    background: linear-gradient(180deg, #fbf7fa 0%, #e9dfe8 30%, #cdbbd2 55%, #8e6fa5 75%, #5c3f7c 100%); }
  .panel--stages { left: 32px; top: 614px; width: 574px; height: 568px;
    background: linear-gradient(180deg, #6a5179 0%, #8a6a96 35%, #b293b2 60%, #e3c4cf 85%, #f1d7dc 100%); }
  .panel--wild { left: 608px; top: 614px; width: 573px; height: 568px;
    background: linear-gradient(180deg, #8a6a92 0%, #b08ca6 35%, #d8b0bb 60%, #f0d2d6 80%, #f6e2e2 100%); }

  .frame { position: absolute; inset: 10px; border: 1px solid var(--frame); }
  .frame::after { content: ""; position: absolute; inset: 3px; border: 1px solid var(--frame); }

  .cover-title { position: absolute; top: 84px; left: 0; width: 100%; text-align: center;
    font-family: "Cinzel", "Trajan Pro", serif; font-weight: 600; font-size: 25px; letter-spacing: 1px;
    color: var(--title-ink); text-shadow: 0 2px 4px rgba(40,0,20,.7); }
  .cover-scene { position: absolute; left: 0; top: 262px; width: 260px; height: 240px;
    background: radial-gradient(circle at 85% 70%, #fbe3c8 0%, #d77a8c 18%, rgba(70,30,60,.6) 55%, rgba(70,30,60,0) 80%); }
  .cover-photo { position: absolute; left: 246px; top: 186px; width: 330px; height: 386px;
    background: linear-gradient(180deg, #b3523f 0%, #c56a55 35%, #e2b2a0 55%, #5a1f3c 75%, #4a1a33 100%);
    border-radius: 140px 140px 0 0; }
  .cover-brand { position: absolute; left: 22px; top: 476px; display: flex; align-items: center; gap: 10px;
    font-family: "Roboto Condensed", sans-serif; font-weight: 300; font-size: 42px; color: var(--logo-purple); }
  .cover-brand__dot { width: 40px; height: 40px; border-radius: 50%; background: var(--logo-purple); }

  .copy { position: absolute; text-align: center; font-style: italic; font-weight: 300;
    font-size: 11.8px; line-height: 16px; color: var(--ink); }
  .copy .head { font-weight: 700; font-style: italic; }
  .gap { height: 16px; }

  .intro-copy { left: 36px; right: 36px; top: 28px; }
  .stages-copy { left: 30px; right: 30px; top: 20px; }
  .wild-copy { left: 30px; right: 28px; top: 20px; }

  .emblem { position: absolute; left: 230px; top: 424px; width: 110px; height: 110px; border-radius: 50%;
    border: 1px solid rgba(120,80,110,.6); background: rgba(240,220,225,.35); }
</style>
</head>
<body>

<section class="panel panel--cover">
  <div class="cover-scene" role="img" aria-label="Silhouetted tree against a glowing sunset over still water"></div>
  <div class="cover-photo" role="img" aria-label="Portrait photograph of the smiling red-haired meditation teacher"></div>
  <h1 class="cover-title">THE RIVER OF PRESENCE MEDITATION</h1>
  <div class="cover-brand"><span class="cover-brand__dot"></span>Mara Vale</div>
</section>

<section class="panel panel--intro">
  <div class="frame"></div>
  <div class="copy intro-copy">
    <p>This meditation is designed so that you can explore and embrace all the<br>energies that are within you - from the wildest to the most still. It is a<br>voyage of discovery that allows you - on a daily basis - to access the<br>energy coming from base chakras such as instinct, sex and power. Once<br>accessed, this energy can be transformed into love and radiance as it<br>moves through your heart. As your life forces moves upward, it opens a<br>channel for your voice and intuition to be expressed and then expands<br>into the boundless spaciousness of eternity. In connecting with all that<br>you are, you come to a deeper acceptance of your own nature, grounded<br>in the earth and enriched by the mystery of spirit. This is very real magic.</p>
    <div class="gap"></div>
    <p class="head">INTIMACY, RELATIONSHIP &amp; TANTRA WORKSHOPS WITH MARA VALE</p>
    <p>Mara Vale, together with her husband Tomas Reyne, leads<br>workshops on sexuality, intimacy and relationships that invite you<br>to live your self totally. In growing a deeper love for yourself, you<br>open to richer, more nourishing relationships.<br>www.maravale.com</p>
    <div class="gap"></div><div class="gap"></div>
    <p>The River of Presence Meditation</p>
    <div class="gap"></div>
    <p>A meditation to open to all that you are<br>A meditation to fly high in your life<br>A meditation to open to your roots and your wings</p>
    <div class="gap"></div><div class="gap"></div>
    <p>All music composed, produced, recorded, mixed and mastered by</p>
    <p class="head" style="font-style:normal">SOLENTRA<br>www.solentra.com</p>
    <p>Lyrics and vocals by MARA VALE<br>Rob Hallet : Percussion on tracks 1 &amp; 2<br>Ezra Lindqvist : djembe on track 1</p>
  </div>
</section>

<section class="panel panel--stages">
  <div class="frame"></div>
  <div class="copy stages-copy">
    <p>For this meditation you'll need a space where you can move freely and preferably have a mattress or soft space<br>for the second and third stages. You'll need a pillow for the second stage.<br>The meditation is in 7 stages that start with movement and move towards stillness.</p>
    <div class="gap"></div>
    <p class="head">The seven stages are:</p>
    <div class="gap"></div>
    <p><b class="head">1 Shaking</b> (standing)<br>
    <b class="head">2 Exploring your wild energy</b> (on the floor or mattress)<br>
    <b class="head">3 Loving yourself in your aliveness</b> (on the floor or mattress)<br>
    <b class="head">4 Journeying up through each of the energy centres or chakras in the body</b><br>(moving mid-way to standing)<br>
    <b class="head">5 Receiving the energy of the infinite standing in that consciousness</b><br>
    <b class="head">6 Guided back into sitting in meditation for 15 minutes</b><br>
    <b class="head">7 Celebration and returning to your day</b></p>
    <div class="gap"></div><div class="gap"></div>
    <p class="head">First stage: Shaking</p>
    <div class="gap"></div>
    <p>Stand with your feet about hip distance apart, feet firmly planted on the floor. Let your knees be soft and begin to let your body bounce, generating the shaking from your knees so that everything from your pelvis upwards can move freely. Be aware of your body's limitations. It's not necessary to shake strongly, it can be a gentle movement. Don't shake violently. If anything hurts or you are concerned about your body, either make the movement more gentle or lie on the floor and shake your limbs or don't do it at all.<br>Try to keep your whole upper body relaxed, letting go of any holding so that everything can shake (gently, not violently) even your head. Shake everything that you are thinking and feeling. Bring everything down into your body so that your focus of attention is in your body's aliveness and not in your head. Let your belly, shoulders and jaw be loose. Let your mouth be a little open and relaxed. Let your breathing be as full and easy.<br>For this stage, keep any sounds inside.</p>
  </div>
</section>

<section class="panel panel--wild">
  <div class="frame"></div>
  <div class="copy wild-copy">
    <p class="head">Second stage: Exploring your wild energy</p>
    <div class="gap"></div>
    <p>It's easier to get into your wild nature if you let yourself be down on the floor so you can roll around, let go and move easily. During this stage you let your body be as wild, free and uninhibited as you can. Start by holding the pillow so that you can use your hands to squeeze it and claw into it. Your mouth may even be biting into the pillow. Make sure you let your hips move. Be uncensored. Let your body have the freedom to move in ways that would be outside its regular habits and pattern. Keep your eyes closed, opening them only to be sure that you aren't going to hit anything. If you can, let your wild sounds come as well as your wild movements. If that would cause problems, direct your sounds into the pillow. This wild energy may have many different flavours, sometimes all at the same time. It could be wildly happy or angry or sexual. Allow whatever arises and let your body lead you. Beware of going into a repeated pattern of getting angry by beating up someone from the past. Be willing to discover all your energies, not just what you know. Be curious about what is going on in you today. Never mind about what was happening last time you did it, let today be new and discover yourself today. Give yourself permission to enjoy your uncensored, wild energy. Breathe fully. Move fully. Use your hands and jaw and pelvis to connect with your wildness.</p>
    <div class="gap"></div>
    <p class="head">Third stage: Loving yourself</p>
    <div class="gap"></div>
    <p>Now that you've let your energy be wild, you'll likely feel a lot of energy running through you. Enjoy! Feel your life, your life energy – whatever shape, color, movement or temperature - flowing inside you. Let your focus move to soft, deep breathing so that you feel more of yourself. Embrace and befriend all that you discover within yourself. Move softly and gently, maybe stroking yourself as you breathe softly but fully as a way of saying a total yes to yourself. Enjoy your aliveness. You can relax and let go into the softness of your body. Keep your body gently moving.</p>
  </div>
  <div class="emblem" role="img" aria-label="Round tree-of-life emblem"></div>
</section>

</body>
</html>
```